Business card design needed

I would like a clean simple buisness card as a freelance makeup artist.The main colours i would like are black, white card (grey tones) with a pop of red or purple. Card mostly white. Double sided. Front side featuring a vector graphic plain face chart-similiar to the LUX/Corvin Halloway design. Face can be partially shown/cropped or in full. Some white space near text at the front - "Rel Dosk MUA" then in smaller text underneath "Make me over" then rest of the contact details.Font is walkway font.

Rel Dosk MUA Make me over m: 0431 768 209 e: relmira_dosk@fernpost.example

```html
<!DOCTYPE html>
<html lang="en">
<head>
<meta charset="utf-8">
<title>Rel Dosk MUA – Business Card</title>
<link href="https://fonts.googleapis.com/css2?family=Questrial&display=swap" rel="stylesheet">
<style>
  :root {
    --page-bg: #ffffff;
    --card-bg: #f4f4f4;
    --card-edge: #e6e6e6;
    --ink: #333333;
    --accent: #e2202a;
    --art-light: #ececec;
    --art-dark: #cfcfcf;
  }
  html, body {
    margin: 0;
    padding: 0;
    width: 1077px;
    height: 1200px;
    overflow: hidden;
    background: var(--page-bg);
    font-family: "Questrial", sans-serif;
    color: var(--ink);
  }
  .canvas {
    position: relative;
    width: 1077px;
    height: 1200px;
  }
  .card {
    position: absolute;
    width: 806px;
    height: 447px;
    background: var(--card-bg);
    border: 1px solid var(--card-edge);
    border-radius: 22px;
    box-sizing: border-box;
    overflow: hidden;
  }
  .card--front { left: 135px; top: 135px; }
  .card--back  { left: 140px; top: 625px; }

  .brand-name {
    position: absolute;
    margin: 0;
    font-size: 33px;
    font-weight: 400;
    color: var(--accent);
    letter-spacing: 0.3px;
    white-space: nowrap;
  }
  .tagline {
    position: absolute;
    margin: 0;
    font-size: 23px;
    color: var(--ink);
    white-space: nowrap;
  }
  .card--front .brand-name { left: 188px; top: 194px; }
  .card--front .tagline    { left: 233px; top: 243px; }

  .card--back .brand-name { left: 116px; top: 122px; }
  .card--back .tagline    { left: 116px; top: 176px; }

  .contact-list {
    position: absolute;
    left: 82px;
    top: 240px;
    margin: 0;
    padding: 0;
    list-style: none;
  }
  .contact-item {
    display: flex;
    align-items: center;
    height: 46px;
    font-size: 28px;
    color: var(--ink);
    white-space: nowrap;
  }
  .contact-icon {
    width: 24px;
    height: 24px;
    margin-right: 16px;
    flex: none;
  }

  .face-art {
    position: absolute;
    width: 250px;
    height: 395px;
    background: linear-gradient(160deg, var(--art-light), var(--art-dark));
    border-radius: 4px;
  }
  .card--front .face-art { left: 555px; top: 27px; }
  .card--back  .face-art { left: 549px; top: 30px; }
</style>
</head>
<body>
<div class="canvas">

  <section class="card card--front">
    <h1 class="brand-name">Rel Dosk MUA</h1>
    <p class="tagline">Make me over</p>
    <div class="face-art" role="img" aria-label="Line-art face chart illustration of a cropped woman's face with hair strands"></div>
  </section>

  <section class="card card--back">
    <h2 class="brand-name">Rel Dosk MUA</h2>
    <p class="tagline">Make me over</p>
    <ul class="contact-list">
      <li class="contact-item">
        <svg class="contact-icon" viewBox="0 0 24 24" aria-hidden="true">
          <rect x="6" y="2" width="12" height="20" rx="2" fill="none" stroke="var(--accent)" stroke-width="2"/>
          <line x1="10" y1="18" x2="14" y2="18" stroke="var(--accent)" stroke-width="2"/>
        </svg>
        0431 768 209
      </li>
      <li class="contact-item">
        <svg class="contact-icon" viewBox="0 0 24 24" aria-hidden="true">
          <rect x="2" y="5" width="20" height="14" rx="1" fill="none" stroke="var(--accent)" stroke-width="2"/>
          <polyline points="2,6 12,13 22,6" fill="none" stroke="var(--accent)" stroke-width="2"/>
        </svg>
        relmira_dosk@fernpost.example
      </li>
    </ul>
    <div class="face-art" role="img" aria-label="Line-art face chart illustration of a cropped woman's face with hair strands"></div>
  </section>

</div>
</body>
</html>
```